To Build a Wordpress Website/Blog Post

I want to build a wordpress website and blog platform for a personal
Transformation project that will also form part of a multi channel/platform offering inc Framelog, podcasts, Huddle, Reelhouse all of which I am looking for help on. I will aim to blog c 1/2 times per week and would like to build an interactive offering that is future proof in terms
Of sizing and extension into another larger brand offering. (Can anyone pls tell me if/why I would Need a coded design? I’m afraid I don’t Know If I need this?). Tha is
Updates

Have now added ‘coded’ as an upgrade so worth allowing more time For designers

All. Just to let you know that I have added ‘coded’ as an upgrade as I want the Wordpress website to Be built as well as designed. Please see MarnBeck.com for the look and feel I want. I do not need the exommerce functionality at this time but if we could have each of those menu items built that would be great. The ones to show are Home, blog, podcast, owens story, contact, resources plus maybe links to Framelog, Huddle and Reelhouse? Many tha ks

Target Market(s)

Men ages 35-60. Corporate, professional crowd for sure but all males globally. Ex athletes, Dads, interested in health and well-being. Endurance athletes. Interested in men’s health inc mental health, burnout, stress, middle age, life switching, potentiality, direction.

Industry/Entity Type

Health And Wellness

Coding

Coded - Design and coding required

Number of Pages Required

5+ page

Font styles to use
Serif
Sans Serif

Colors
3277b5
33a6d7
0493ce
acd136
1b1b1b
b1b1b1
b2b2b2
dddddd

Requirements
Must have
• A professional but inspirational appearance. Wordpress platform. Needs to host blogs and podcasts and images and feedback/forums plus archives and linking into a multi channel/platform offering. I need to
• Own the ip, be able to post text and images from mobile. It must be responsive and inc my logos and be editable by me at any time/registered in my Name. I enjoy greyscale and muted shades but will highlight other colours below
Nice to have
• See marnbeck for high production values. This will Appeal to professionals (mostly men) that are aged 35-60 and interested in transformation. The idea is to do 50 things by the time I am 50 (Nov 19). So will update and blog etc but also Link to podcasts and Framelog and fbook etc
Should not have
• Too many cliches. Poor design and low production values. Needs to be aspirational

```html
<!DOCTYPE html>
<html lang="en">
<head>
<meta charset="utf-8">
<title>Orlith Fifty</title>
<link href="https://fonts.googleapis.com/css2?family=Oswald:wght@500;600&family=Montserrat:wght@500;600;700&family=Lato:wght@400;700&display=swap" rel="stylesheet">
<style>
:root{
  --green:#acd136;
  --blue:#0493ce;
  --blue-light:#33a6d7;
  --ink:#1b1b1b;
  --grey:#b1b1b1;
  --grey-pale:#dddddd;
  --panel:#f1f1f1;
  --dark:#3c3c3c;
  --white:#ffffff;
}
*{box-sizing:border-box;margin:0;padding:0}
html,body{width:1200px;height:3191px;overflow:hidden}
body{font-family:'Lato',sans-serif;color:var(--ink);background:var(--white);position:relative}
a{color:inherit;text-decoration:none}
.container{width:1000px;margin:0 auto}

/* header */
.site-header{height:119px;display:flex;align-items:center;justify-content:space-between;padding:0 96px 0 100px}
.brand{display:flex;align-items:center;gap:12px;font-family:'Montserrat',sans-serif;font-weight:700;font-size:22px;color:var(--ink)}
.brand-dot{width:22px;height:22px;border-radius:50%;background:var(--green)}
.main-nav{display:flex;gap:58px;font-family:'Montserrat',sans-serif;font-weight:600;font-size:16px;letter-spacing:.3px}

/* hero */
.hero{position:relative;height:515px;background:linear-gradient(160deg,#8a4a3c 0%,#6e5a52 35%,#4a4748 65%,#7b6a5a 100%);color:var(--white);text-align:center}
.hero-copy{position:absolute;left:0;right:0;top:94px}
.hero h1{font-family:'Oswald',sans-serif;font-weight:600;font-size:50px;letter-spacing:.5px}
.hero p{font-family:'Montserrat',sans-serif;font-weight:600;font-size:15px;line-height:26px;width:670px;margin:22px auto 0}
.btn-white{display:inline-block;margin-top:34px;background:var(--white);color:var(--ink);font-family:'Montserrat',sans-serif;font-weight:700;font-size:16px;padding:15px 14px}
.hero-arrow{position:absolute;top:232px}
.hero-arrow.prev{left:34px}
.hero-arrow.next{right:34px}

/* feature tiles */
.tiles{height:281px;background:var(--grey-pale);display:flex;gap:10px;padding:9px 8px}
.tile{flex:1;position:relative;display:flex;align-items:flex-end;justify-content:center;padding-bottom:18px}
.tile span{font-family:'Oswald',sans-serif;font-weight:500;font-size:23px;color:var(--white)}
.tile-1{background:linear-gradient(135deg,#b9c7d3,#6a8aa4 60%,#3e5d78)}
.tile-2{background:linear-gradient(135deg,#3b3b3f,#8a7c7a 55%,#2b2b2e)}
.tile-3{background:linear-gradient(135deg,#7e5436,#c99a6a 50%,#2e6f8a)}

/* section heading */
.section{text-align:center}
.section-title{font-family:'Oswald',sans-serif;font-weight:600;font-size:31px;color:var(--blue)}
.rule{width:58px;height:2px;background:var(--blue);margin:20px auto 0}

/* about */
.about{height:455px;padding-top:84px}
.about p{font-size:14.5px;line-height:23px;margin:0 auto;width:990px}
.about .rule{margin-bottom:36px}
.about p+p{margin-top:10px}
.btn{display:inline-block;color:var(--white);font-family:'Lato',sans-serif;font-weight:700;font-size:15px;padding:14px 22px}
.btn-green{background:var(--green)}
.btn-blue{background:var(--blue)}
.about .btn{margin-top:30px}

/* cards */
.podcasts{height:596px;background:var(--panel);padding-top:62px}
.blog{height:600px;padding-top:68px}
.cards{display:flex;justify-content:space-between;margin-top:48px}
.podcasts .cards{margin-top:44px}
.card{width:315px;text-align:center}
.card-media{height:175px;position:relative;display:flex;justify-content:center;padding-top:60px}
.card-label{position:relative;margin:-16px auto 0;width:278px;padding:18px 0;color:var(--white);font-family:'Montserrat',sans-serif;font-weight:600;font-size:15px}
.card p{font-size:13.5px;line-height:21px;margin:22px auto 0;width:290px}
.card .btn{margin-top:24px}
.card h3{font-family:'Montserrat',sans-serif;font-weight:700;font-size:18.5px;margin-top:28px}
.card h3+p{margin-top:14px}
.m-p1{background:linear-gradient(135deg,#5c6a66,#a9b0aa 55%,#3e4743)}
.m-p2{background:linear-gradient(135deg,#4d6b3a,#8fa36c 55%,#9c7f6b)}
.m-p3{background:linear-gradient(135deg,#6c6b67,#c7883a 55%,#8b8c8a)}
.m-b1{background:linear-gradient(135deg,#d9d3c7,#a8987f 55%,#6e7e8f)}
.m-b2{background:linear-gradient(135deg,#1f2a2e,#5a6a62 55%,#2d3130)}
.m-b3{background:linear-gradient(135deg,#5a5a5e,#c4a185 55%,#3a3a3e)}

/* connect */
.connect{height:205px;background:var(--dark);border-bottom:4px solid var(--green);display:flex;align-items:center;padding:0 0 0 100px}
.connect-intro{width:302px;flex:none;color:var(--white)}
.connect-intro h2{font-family:'Oswald',sans-serif;font-weight:600;font-size:33px}
.connect-intro p{font-size:17px;margin-top:8px}
.socials{display:flex;width:715px;flex:none;justify-content:space-between}
.social{width:140px;text-align:center;color:var(--white);font-family:'Montserrat',sans-serif;font-weight:700;font-size:16px}
.social i{display:block;width:68px;height:68px;border-radius:50%;background:var(--white);margin:0 auto 16px}
.social.active i{background:var(--green)}

/* footer */
.site-footer{height:357px;background:var(--panel);display:flex;padding:70px 0 0 92px}
.footer-brand{width:298px;display:flex;align-items:center;gap:12px;height:200px;font-family:'Montserrat',sans-serif;font-weight:700;font-size:24px}
.footer-brand .brand-dot{width:26px;height:26px}
.footer-col h4{font-family:'Montserrat',sans-serif;font-weight:700;font-size:15.5px;color:var(--blue)}
.footer-col .rule{margin:14px 0 0}
.quick{width:172px}
.quick ul{list-style:none;margin-top:24px}
.quick li{font-size:14.5px;line-height:32px}
.quick li::before{content:"›";margin-right:8px}
.contact{width:298px}
.contact-item{display:flex;gap:16px;margin-top:24px}
.contact-item:first-of-type{margin-top:28px}
.contact-icon{width:40px;height:40px;border-radius:50%;border:2px solid var(--blue);display:flex;align-items:center;justify-content:center;flex:none}
.contact-item strong{font-family:'Montserrat',sans-serif;font-size:14px;display:block;margin-top:2px}
.contact-item span{font-size:12.5px;line-height:20px;display:block;margin-top:4px}
.form-col{width:240px}
.form{margin-top:24px;display:grid;grid-template-columns:1fr 1fr;gap:10px}
.field{height:34px;border:1px solid var(--grey);background:var(--white);font-size:11px;padding:9px 8px}
.field.full{grid-column:1/3;height:64px}
.btn-send{grid-column:1/2;width:118px;margin-top:6px;background:var(--green);color:var(--white);font-family:'Montserrat',sans-serif;font-weight:600;font-size:12px;padding:12px 0;text-align:center}
.copyright{height:63px;background:var(--blue);color:var(--white);display:flex;align-items:center;justify-content:center;font-family:'Montserrat',sans-serif;font-weight:600;font-size:14.5px}
</style>
</head>
<body>

<header class="site-header">
  <a class="brand" href="#"><span class="brand-dot"></span>Orlith Fifty</a>
  <nav class="main-nav">
    <a href="#">HOME</a><a href="#">ABOUT</a><a href="#">PODCAST</a><a href="#">FAQ</a><a href="#">RESOURCES</a><a href="#">CONTACT</a>
  </nav>
</header>

<section class="hero" role="img" aria-label="Friends sitting together on a rooftop overlooking the city">
  <div class="hero-copy">
    <h1>THINGS TO DO BEFORE 50 AGE</h1>
    <p>Duis aute irure dolor in reprehenderit in voluptate velit esse cillum dolore eu fugiat nulla pariatur.</p>
    <a class="btn-white" href="#">Read More</a>
  </div>
  <svg class="hero-arrow prev" width="26" height="52" viewBox="0 0 26 52"><polyline points="24,2 2,26 24,50" fill="none" stroke="#fff" stroke-width="2"/></svg>
  <svg class="hero-arrow next" width="26" height="52" viewBox="0 0 26 52"><polyline points="2,2 24,26 2,50" fill="none" stroke="#fff" stroke-width="2"/></svg>
</section>

<section class="tiles">
  <div class="tile tile-1" role="img" aria-label="Man running along the coast"><span>NEMO ENIM IPSAM</span></div>
  <div class="tile tile-2" role="img" aria-label="Speaker holding a microphone"><span>NEMO ENIM IPSAM</span></div>
  <div class="tile tile-3" role="img" aria-label="Couple sharing a meal"><span>NEMO ENIM IPSAM</span></div>
</section>

<section class="section about">
  <h2 class="section-title">ABOUT ORLITH FIFTY</h2>
  <div class="rule"></div>
  <p>Sed ut perspiciatis unde omnis iste natus error sit voluptatem accusantium doloremque lau dantium, totam rem aperiam, eaque ipsa quae ab illo inventore veritatis et quasi archi tecto beatae vitae dicta sunt explicabo.</p>
  <p>Nemo enim ipsam voluptatem quia voluptas sit aspernatur aut odit aut fugit, sed quia conse quuntur magni dolores eos qui ratione voluptatem sequi nesciunt. Neque porro quisquam est, qui dolorem ipsum quia dolor sit amet, consectetur, adipisci velit.</p>
  <a class="btn btn-green" href="#">Read More</a>
</section>

<section class="section podcasts">
  <h2 class="section-title">OUR PODCAST</h2>
  <div class="rule"></div>
  <div class="container cards">
    <article class="card">
      <div class="card-media m-p1" role="img" aria-label="Man working on a laptop outdoors">
        <svg width="50" height="46" viewBox="0 0 50 46"><path d="M5 30V24a20 20 0 0 1 40 0v6" fill="none" stroke="#fff" stroke-width="3"/><rect x="3" y="28" width="9" height="15" rx="3" fill="none" stroke="#fff" stroke-width="3"/><rect x="38" y="28" width="9" height="15" rx="3" fill="none" stroke="#fff" stroke-width="3"/></svg>
      </div>
      <div class="card-label btn-green">Podcast Dale Mercer Voss</div>
      <p>Duis aute irure dolor in reprehenderit in voluptate velit esse cillum dolorem.</p>
      <a class="btn btn-green" href="#">Listen Now</a>
    </article>
    <article class="card">
      <div class="card-media m-p2" role="img" aria-label="Man reading a newspaper in a garden">
        <svg width="50" height="46" viewBox="0 0 50 46"><path d="M5 30V24a20 20 0 0 1 40 0v6" fill="none" stroke="#fff" stroke-width="3"/><rect x="3" y="28" width="9" height="15" rx="3" fill="none" stroke="#fff" stroke-width="3"/><rect x="38" y="28" width="9" height="15" rx="3" fill="none" stroke="#fff" stroke-width="3"/></svg>
      </div>
      <div class="card-label btn-blue">Podcast Grant Ellory</div>
      <p>Duis aute irure dolor in reprehenderit in voluptate velit esse cillum dolorem.</p>
      <a class="btn btn-blue" href="#">Listen Now</a>
    </article>
    <article class="card">
      <div class="card-media m-p3" role="img" aria-label="Older couple in warm jackets by a stone wall">
        <svg width="50" height="46" viewBox="0 0 50 46"><path d="M5 30V24a20 20 0 0 1 40 0v6" fill="none" stroke="#fff" stroke-width="3"/><rect x="3" y="28" width="9" height="15" rx="3" fill="none" stroke="#fff" stroke-width="3"/><rect x="38" y="28" width="9" height="15" rx="3" fill="none" stroke="#fff" stroke-width="3"/></svg>
      </div>
      <div class="card-label btn-green">Podcast Coach Milo Hart</div>
      <p>Duis aute irure dolor in reprehenderit in voluptate velit esse cillum dolorem.</p>
      <a class="btn btn-green" href="#">Listen Now</a>
    </article>
  </div>
</section>

<section class="section blog">
  <h2 class="section-title">OUR BLOG POSTS</h2>
  <div class="rule"></div>
  <div class="container cards">
    <article class="card">
      <div class="card-media m-b1" role="img" aria-label="Couple dining together"></div>
      <h3>DUIS AUTE IRURE DOLOR</h3>
      <p>Duis aute irure dolor in reprehenderit in voluptate velit esse cillum dolorem.</p>
      <a class="btn btn-green" href="#">Read More</a>
    </article>
    <article class="card">
      <div class="card-media m-b2" role="img" aria-label="Man reading a book at a desk"></div>
      <h3>DUIS AUTE IRURE DOLOR</h3>
      <p>Duis aute irure dolor in reprehenderit in voluptate velit esse cillum dolorem.</p>
      <a class="btn btn-blue" href="#">Read More</a>
    </article>
    <article class="card">
      <div class="card-media m-b3" role="img" aria-label="Man doing push-ups on a mat"></div>
      <h3>DUIS AUTE IRURE DOLOR</h3>
      <p>Duis aute irure dolor in reprehenderit in voluptate velit esse cillum dolorem.</p>
      <a class="btn btn-green" href="#">Read More</a>
    </article>
  </div>
</section>

<section class="connect">
  <div class="connect-intro">
    <h2>CONNECT WITH US:</h2>
    <p>Through social networks</p>
  </div>
  <div class="socials">
    <a class="social" href="#"><i></i>HUDDLE</a>
    <a class="social active" href="#"><i></i>CHIRP</a>
    <a class="social" href="#"><i></i>REELHOUSE</a>
    <a class="social" href="#"><i></i>FRAMELOG</a>
    <a class="social" href="#"><i></i>FLASHTALK</a>
  </div>
</section>

<footer class="site-footer">
  <div class="footer-brand"><span class="brand-dot"></span>Orlith Fifty</div>
  <div class="footer-col quick">
    <h4>QUICK LINKS</h4>
    <div class="rule"></div>
    <ul><li>Home</li><li>About</li><li>Podcast</li><li>FAQ</li><li>Resources</li><li>Contact Us</li></ul>
  </div>
  <div class="footer-col contact">
    <h4>CONTACT US</h4>
    <div class="rule"></div>
    <div class="contact-item">
      <div class="contact-icon"><svg width="14" height="20" viewBox="0 0 14 20"><path d="M7 1a6 6 0 0 1 6 6c0 5-6 12-6 12S1 12 1 7a6 6 0 0 1 6-6z" fill="none" stroke="#0493ce" stroke-width="2"/><circle cx="7" cy="7" r="2" fill="#0493ce"/></svg></div>
      <div><strong>ADDRESS,</strong><span>48 Harbor Lane<br>210 Westbrook, OR 97012</span></div>
    </div>
    <div class="contact-item">
      <div class="contact-icon"><svg width="12" height="20" viewBox="0 0 12 20"><rect x="1" y="1" width="10" height="18" rx="2" fill="none" stroke="#0493ce" stroke-width="2"/><circle cx="6" cy="15" r="1.2" fill="#0493ce"/></svg></div>
      <div><strong>PHONE:</strong><span>555 014 7788</span></div>
    </div>
    <div class="contact-item">
      <div class="contact-icon"><svg width="18" height="14" viewBox="0 0 18 14"><rect x="1" y="1" width="16" height="12" fill="none" stroke="#0493ce" stroke-width="2"/><polyline points="1,1 9,8 17,1" fill="none" stroke="#0493ce" stroke-width="2"/></svg></div>
      <div><strong>Mail:</strong><span>hello@orlithfifty.com</span></div>
    </div>
  </div>
  <div class="footer-col form-col">
    <h4>CONTACT FORM</h4>
    <div class="rule"></div>
    <div class="form">
      <div class="field">Name</div>
      <div class="field">Phone</div>
      <div class="field full">Message</div>
      <div class="btn-send">SEND MESSAGE</div>
    </div>
  </div>
</footer>

<div class="copyright">Copyright © 2018 Orlith Fifty. All Rights Reserved.</div>

</body>
</html>
```